KVO-Business Card Design

I need a modern, professional business card design that includes my logo as the main feature, maybe the entire background with the contact info overlaying or even contact info on the back and the logo full frontal

Neat and organized placement of contact information

Would like to see options in black and white

Target Market(s)

real estate Developers, Construction managers, business and home owners

Industry/Entity Type

Construction

Contact Information for Business Card

KVO Construction
Danny Ferrante
General Contractor

Office: 1-888-902-7315 Ext #1
Cell: 215-730-4162
Fax: 1-888-902-7315

Font styles to use
Serif

Requirements
Must have
• title
• office #
• cell #
• Email
• website
Nice to have
• fax

```html
<!DOCTYPE html>
<html lang="en">
<head>
<meta charset="utf-8">
<title>KVO Construction – Business Card</title>
<link rel="stylesheet" href="https://fonts.googleapis.com/css2?family=Source+Serif+4:wght@400;600;700&display=swap">
<style>
  :root {
    --board: #2b2b2b;
    --card: #ffffff;
    --brand-green: #3f9a3c;
    --ink: #111111;
    --mark-grey: #8a8a8a;
    --ghost: #e8e8e8;
  }
  * { margin: 0; padding: 0; box-sizing: border-box; }
  html, body {
    width: 1200px; height: 1200px; overflow: hidden;
    background: var(--board);
    font-family: "Source Serif 4", Georgia, "Times New Roman", serif;
  }
  .board { position: relative; width: 1200px; height: 1200px; }
  .card { position: absolute; background: var(--card); overflow: hidden; }
  .card--front { left: 210px; top: 74px; width: 769px; height: 406px; }
  .card--back  { left: 215px; top: 656px; width: 770px; height: 406px; }

  .front-brand {
    position: absolute; left: 0; right: 0; top: 120px;
    display: flex; justify-content: center; align-items: center; gap: 22px;
  }
  .front-name {
    font-weight: 700; font-size: 150px; line-height: 1;
    letter-spacing: 4px; color: var(--brand-green);
  }
  .front-square {
    width: 34px; height: 34px; background: var(--brand-green);
  }

  .ghost-name {
    position: absolute; left: 390px; top: 70px;
    font-weight: 700; font-size: 250px; line-height: 1;
    color: var(--ghost); white-space: nowrap;
  }

  .back-mark {
    position: absolute; left: 0; width: 410px; top: 52px;
    text-align: center;
    font-weight: 700; font-size: 30px; line-height: 1;
    color: var(--mark-grey); letter-spacing: 1px;
  }
  .company {
    position: absolute; left: 0; width: 410px; top: 112px;
    text-align: center;
    font-weight: 700; font-size: 22px; line-height: 1.2; color: var(--ink);
  }
  .person {
    position: absolute; left: 0; width: 426px; top: 170px;
    text-align: center; color: var(--ink);
  }
  .person__name { font-size: 29px; font-weight: 400; line-height: 1.15; }
  .person__title { font-size: 11px; margin-top: 2px; }

  .contact {
    position: absolute; left: 117px; top: 272px;
    font-size: 15px; line-height: 21px; color: var(--ink);
    list-style: none;
  }
  .contact__label { display: inline-block; width: 60px; }
</style>
</head>
<body>
<main class="board">
  <section class="card card--front" aria-label="Card front">
    <div class="front-brand">
      <span class="front-name">KVO</span>
      <span class="front-square" aria-hidden="true"></span>
    </div>
  </section>

  <section class="card card--back" aria-label="Card back">
    <div class="ghost-name" aria-hidden="true">KVO</div>
    <div class="back-mark">KVO</div>
    <h1 class="company">KVO Construction</h1>
    <div class="person">
      <p class="person__name">Danny Ferrante</p>
      <p class="person__title">General Contractor</p>
    </div>
    <ul class="contact">
      <li><span class="contact__label">Office:</span>1-888-902-7315 Ext #1</li>
      <li><span class="contact__label">Cell:</span>215-730-4162</li>
      <li><span class="contact__label">Fax:</span>1-888-902-7315</li>
      <li><span class="contact__label">Email:</span>danny@kvoconstruction.com</li>
      <li><span class="contact__label">Web:</span>www.kvoconstruction.com</li>
    </ul>
  </section>
</main>
</body>
</html>
```